Landing Page & Logo for Over 50s Guaranteed Life Cover

www.silverquoteway.com provides a method of comparing guaranteed life cover for consumers aged over 50. The approach we are initially looking to deploy is a simple landing page that provides the user with high level information about SilverQuoteWay and allows them to see which provider is offering the best deal by ranking providers in a table. This will compare costs / core features in the same way as shown in the attached file.

The page should incorporate a new logo design for SilverQuoteWay.com which should be similar in design to the website greyharbourcover.com.

Key elements of the landing page include:

Header (incorporating new logo and strapline e.g. "helping you find the best cover at the best price")
Introductory Text (to allow brief description of the service)
Comparison Table (to show top 10 providers - to include logos)
Table Links (allows customer to link directly from the table to the providers site)
Helpline (details of helpline number 0800 317 2946 - not actual number)
Join The Club (allows customers to sign up - using their email - to the over 50s club for more information and offers)

Other design elements welcomed to ensure the landing page is simple to understand, easy to navigate, visually appealing, focused on driving action / sales.

Additional payment approx. £60 for incorporating a new logo. Added Monday, April 25, 2016

Target Market(s)

50 - 80

Industry/Entity Type

Insurance

Logo Text

silverquoteway and strapline "helping you find the best cover at the best price"

Number of Pages Required

1 page

Font styles to use
Sans Serif

Colors
a5ce39
add136
cadf82
eaf2ce
ffffff

Requirements
Nice to have
• Ideally created so content can be managed via WordPress.

```html
<!DOCTYPE html>
<html lang="en">
<head>
<meta charset="utf-8">
<title>SilverQuoteWay.com – Compare Guaranteed Life Cover</title>
<link rel="stylesheet" href="https://fonts.googleapis.com/css2?family=Mulish:ital,wght@0,700;0,800;1,800&family=Noto+Serif:wght@400;700&family=Roboto:wght@400;500;700&display=swap">
<style>
:root{
  --lime:#a5ce39;
  --lime-bright:#add136;
  --olive:#84aa14;
  --tagline:#6f9215;
  --cream:#f9fbea;
  --navy:#1e2838;
  --table-green:#4cb04c;
  --footer-green:#3e5d0c;
  --orange:#f47b2a;
  --blue:#1b84c7;
  --info:#1a9ad6;
  --text:#555b60;
  --white:#ffffff;
  --header-bg:#f6f6f6;
}
*{box-sizing:border-box;margin:0;padding:0}
html,body{width:1200px;height:2667px;overflow:hidden}
body{position:relative;font-family:"Roboto",Arial,sans-serif;color:var(--text);background:var(--white)}
.abs{position:absolute}

/* header */
.site-header{top:0;left:0;width:1200px;height:208px;background:var(--header-bg)}
.brand{position:absolute;display:flex;align-items:center;gap:12px;font-family:"Mulish",sans-serif;font-weight:800;color:var(--lime)}
.brand-dot{border-radius:50%;background:var(--lime)}
.site-header .brand{top:50px;left:0;width:1200px;justify-content:center;font-size:46px}
.site-header .brand-dot{width:34px;height:34px}
.tagline{position:absolute;top:143px;width:1200px;text-align:center;font-family:"Noto Serif",serif;font-weight:700;font-size:23px;color:var(--tagline);letter-spacing:.3px}

/* nav */
.main-nav{top:208px;left:0;width:1200px;height:45px;background:var(--navy)}
.main-nav a{position:absolute;top:12px;transform:translateX(-50%);font-family:"Noto Serif",serif;font-size:16px;color:var(--lime-bright);text-decoration:none;white-space:nowrap}

/* hero */
.hero{top:253px;left:0;width:1200px;height:410px;background:linear-gradient(180deg,#5f9fdc 0%,#8cc0ec 45%,#c9e2f6 82%,#6fa83a 88%,#4b8a22 100%)}
.hero-title{position:absolute;left:604px;top:122px;width:420px;font-family:"Roboto",sans-serif;font-weight:700;font-size:36px;line-height:36px;color:var(--white);text-transform:uppercase}
.hero-text{position:absolute;left:608px;top:212px;width:410px;font-size:15.5px;line-height:19px;color:var(--white)}
.hero-btn{position:absolute;left:610px;top:286px;width:169px;height:41px;background:var(--navy);color:var(--lime-bright);font-family:"Noto Serif",serif;font-size:13px;display:flex;align-items:center;justify-content:center}

/* compare */
.compare{top:663px;left:0;width:1200px;height:1262px;background:var(--cream)}
.section-title{position:absolute;left:0;width:1200px;text-align:center;font-family:"Mulish",sans-serif;font-style:italic;font-weight:800;font-size:37px;color:var(--olive)}
.title-rule{position:absolute;left:563px;width:75px;height:3px;background:var(--olive)}
.intro{position:absolute;left:0;width:1200px;text-align:center;font-size:13.5px;line-height:19px;color:var(--text)}

.compare-table{position:absolute;left:128px;top:235px;width:908px;height:995px;background:var(--table-green)}
.table-head,.table-row{position:absolute;left:14px;width:880px;display:grid;grid-template-columns:142px 144px 96px 128px 164px 100px 106px}
.table-head{top:16px;height:48px;background:var(--navy)}
.table-head span{display:flex;align-items:center;justify-content:center;color:var(--white);font-size:12.5px}
.table-row{height:76px;background:var(--white)}
.cell{display:flex;flex-direction:column;align-items:center;justify-content:center;gap:7px;font-size:11.5px;color:#444}
.cell.amount{font-size:17px;color:#222}
.row-feature .cell.amount{font-weight:700}
.provider{font-family:"Roboto",sans-serif;font-weight:700;font-size:21px;color:var(--info);letter-spacing:.5px}
.info{width:16px;height:16px;border-radius:50%;background:var(--info);color:var(--white);font-size:11px;font-weight:700;font-family:"Noto Serif",serif;display:flex;align-items:center;justify-content:center;line-height:1}
.btn-buy,.btn-more{width:93px;height:28px;display:flex;align-items:center;justify-content:center;gap:5px;color:var(--white);font-size:10px;font-weight:500;border-radius:2px}
.btn-buy{background:var(--orange)}
.btn-more{background:var(--blue)}
.cell.actions{gap:5px}
.caret{width:0;height:0;border-top:3px solid transparent;border-bottom:3px solid transparent;border-left:4px solid var(--white)}
.load-more{position:absolute;left:348px;top:933px;width:214px;height:36px;border:2px solid var(--white);color:var(--white);font-size:13px;display:flex;align-items:center;justify-content:center}

/* about */
.about{top:1925px;left:0;width:1200px;height:297px;background:var(--white)}
.about a{color:#1f5fb5;font-style:italic;font-weight:700;text-decoration:underline}
.cta-btn{position:absolute;left:476px;top:226px;width:212px;height:32px;background:var(--lime);color:#33410c;font-size:13px;display:flex;align-items:center;justify-content:center}

/* footer */
.site-footer{top:2222px;left:0;width:1200px;height:343px;background:var(--footer-green)}
.site-footer .brand{top:28px;left:151px;font-size:30px}
.site-footer .brand-dot{width:24px;height:24px}
.helpline{position:absolute;left:759px;top:38px;color:var(--white);font-size:13px;display:flex;align-items:baseline;gap:6px}
.helpline strong{font-size:22px;font-weight:700}
.dash{position:absolute;left:142px;width:877px;border-top:2px dashed var(--lime)}
.club-title{position:absolute;top:118px;left:0;width:1200px;text-align:center;font-family:"Mulish",sans-serif;font-style:italic;font-weight:800;font-size:28px;color:var(--lime)}
.club-text{position:absolute;top:163px;left:0;width:1200px;text-align:center;font-size:12px;color:var(--white)}
.signup{position:absolute;left:279px;top:210px;display:flex}
.signup .email{width:503px;height:36px;background:var(--white);color:#666;font-size:12px;display:flex;align-items:center;padding-left:14px}
.signup .subscribe{width:91px;height:36px;background:var(--lime);color:#2d3b0b;font-size:13px;display:flex;align-items:center;justify-content:center}
.queries{position:absolute;top:302px;left:0;width:1200px;text-align:center;font-size:12px;color:var(--white)}
.queries a{color:#4fb7e8;font-style:italic;text-decoration:underline}

/* bottom bar */
.bottom-bar{top:2565px;left:0;width:1200px;height:102px;background:var(--navy)}
.legal-links{position:absolute;top:17px;left:0;width:1200px;display:flex;justify-content:center;gap:18px;font-size:11px;color:var(--lime)}
.legal-links .sep{color:var(--lime)}
.copyright{position:absolute;top:56px;left:0;width:1200px;text-align:center;font-size:10.5px;color:var(--white)}
</style>
</head>
<body>

<header class="site-header abs">
  <div class="brand"><span>SilverQuoteWay.com</span><span class="brand-dot"></span></div>
  <p class="tagline">HELPING YOU FIND THE BEST COVER AT THE BEST PRICE</p>
</header>

<nav class="main-nav abs">
  <a style="left:236px">HOME</a>
  <a style="left:379px">LIFE INSURANCE</a>
  <a style="left:580px">OTHER INSURANCES</a>
  <a style="left:763px">FREE QUOTE</a>
  <a style="left:901px">CONTACT</a>
</nav>

<section class="hero abs" role="img" aria-label="Photo of a child holding a rainbow umbrella on a grassy field under a blue sky">
  <h1 class="hero-title">Worried about life insurance plans?</h1>
  <p class="hero-text">SilverQuoteWay has teamed up with our friends at Brightwell to bring you high quality low cost cover from leading insurers.</p>
  <div class="hero-btn">Retrieve A Quote</div>
</section>

<section class="compare abs">
  <h2 class="section-title" style="top:22px">Compare Guaranteed Life Cover</h2>
  <div class="title-rule" style="top:76px"></div>
  <p class="intro" style="top:104px">Looking for guaranteed life cover without the need to answer lots of medical questions or go for a medical?<br>To make things simple, below we've compared cover from a selection of providers.</p>
  <p class="intro" style="top:152px">Simply click on the Buy Now button to get a personalised quote, or click the More Info button if you need<br>more information about the cover.</p>

  <div class="compare-table">
    <div class="table-head">
      <span>Company Name</span><span>Cover Amount</span><span>Premium</span><span>Payment Term</span><span>Total Payment</span><span>Initial Period</span><span>Buy Now</span>
    </div>

    <div class="table-row row-feature" style="top:71px">
      <div class="cell"><span class="provider">NORTHMERE</span></div>
      <div class="cell amount">£4,200<span class="info">i</span></div>
      <div class="cell">£10.00<span class="info">i</span></div>
      <div class="cell">40 years<span class="info">i</span></div>
      <div class="cell">£4,800.00<span class="info">i</span></div>
      <div class="cell">24 months<span class="info">i</span></div>
      <div class="cell actions"><span class="btn-buy">BUY NOW<i class="caret"></i></span><span class="btn-more">MORE INFO<i class="caret"></i></span></div>
    </div>
    <div class="table-row row-feature" style="top:156px">
      <div class="cell"><span class="provider">NORTHMERE</span></div>
      <div class="cell amount">£4,200<span class="info">i</span></div>
      <div class="cell">£10.00<span class="info">i</span></div>
      <div class="cell">40 years<span class="info">i</span></div>
      <div class="cell">£4,800.00<span class="info">i</span></div>
      <div class="cell">24 months<span class="info">i</span></div>
      <div class="cell actions"><span class="btn-buy">BUY NOW<i class="caret"></i></span><span class="btn-more">MORE INFO<i class="caret"></i></span></div>
    </div>
    <div class="table-row row-feature" style="top:241px">
      <div class="cell"><span class="provider">NORTHMERE</span></div>
      <div class="cell amount">£4,200<span class="info">i</span></div>
      <div class="cell">£10.00<span class="info">i</span></div>
      <div class="cell">40 years<span class="info">i</span></div>
      <div class="cell">£4,800.00<span class="info">i</span></div>
      <div class="cell">24 months<span class="info">i</span></div>
      <div class="cell actions"><span class="btn-buy">BUY NOW<i class="caret"></i></span><span class="btn-more">MORE INFO<i class="caret"></i></span></div>
    </div>
    <div class="table-row row-feature" style="top:326px">
      <div class="cell"><span class="provider">NORTHMERE</span></div>
      <div class="cell amount">£4,200<span class="info">i</span></div>
      <div class="cell">£10.00<span class="info">i</span></div>
      <div class="cell">40 years<span class="info">i</span></div>
      <div class="cell">£4,800.00<span class="info">i</span></div>
      <div class="cell">24 months<span class="info">i</span></div>
      <div class="cell actions"><span class="btn-buy">BUY NOW<i class="caret"></i></span><span class="btn-more">MORE INFO<i class="caret"></i></span></div>
    </div>
    <div class="table-row" style="top:411px">
      <div class="cell"><span class="provider">NORTHMERE</span></div>
      <div class="cell amount">£4,200<span class="info">i</span></div>
      <div class="cell">£10.00<span class="info">i</span></div>
      <div class="cell">40 years<span class="info">i</span></div>
      <div class="cell">£4,800.00<span class="info">i</span></div>
      <div class="cell">24 months<span class="info">i</span></div>
      <div class="cell actions"><span class="btn-buy">BUY NOW<i class="caret"></i></span><span class="btn-more">MORE INFO<i class="caret"></i></span></div>
    </div>
    <div class="table-row" style="top:496px">
      <div class="cell"><span class="provider">NORTHMERE</span></div>
      <div class="cell amount">£4,200<span class="info">i</span></div>
      <div class="cell">£10.00<span class="info">i</span></div>
      <div class="cell">40 years<span class="info">i</span></div>
      <div class="cell">£4,800.00<span class="info">i</span></div>
      <div class="cell">24 months<span class="info">i</span></div>
      <div class="cell actions"><span class="btn-buy">BUY NOW<i class="caret"></i></span><span class="btn-more">MORE INFO<i class="caret"></i></span></div>
    </div>
    <div class="table-row" style="top:581px">
      <div class="cell"><span class="provider">NORTHMERE</span></div>
      <div class="cell amount">£4,200<span class="info">i</span></div>
      <div class="cell">£10.00<span class="info">i</span></div>
      <div class="cell">40 years<span class="info">i</span></div>
      <div class="cell">£4,800.00<span class="info">i</span></div>
      <div class="cell">24 months<span class="info">i</span></div>
      <div class="cell actions"><span class="btn-buy">BUY NOW<i class="caret"></i></span><span class="btn-more">MORE INFO<i class="caret"></i></span></div>
    </div>
    <div class="table-row" style="top:666px">
      <div class="cell"><span class="provider">NORTHMERE</span></div>
      <div class="cell amount">£4,200<span class="info">i</span></div>
      <div class="cell">£10.00<span class="info">i</span></div>
      <div class="cell">40 years<span class="info">i</span></div>
      <div class="cell">£4,800.00<span class="info">i</span></div>
      <div class="cell">24 months<span class="info">i</span></div>
      <div class="cell actions"><span class="btn-buy">BUY NOW<i class="caret"></i></span><span class="btn-more">MORE INFO<i class="caret"></i></span></div>
    </div>
    <div class="table-row" style="top:751px">
      <div class="cell"><span class="provider">NORTHMERE</span></div>
      <div class="cell amount">£4,200<span class="info">i</span></div>
      <div class="cell">£10.00<span class="info">i</span></div>
      <div class="cell">40 years<span class="info">i</span></div>
      <div class="cell">£4,800.00<span class="info">i</span></div>
      <div class="cell">24 months<span class="info">i</span></div>
      <div class="cell actions"><span class="btn-buy">BUY NOW<i class="caret"></i></span><span class="btn-more">MORE INFO<i class="caret"></i></span></div>
    </div>
    <div class="table-row" style="top:836px">
      <div class="cell"><span class="provider">NORTHMERE</span></div>
      <div class="cell amount">£4,200<span class="info">i</span></div>
      <div class="cell">£10.00<span class="info">i</span></div>
      <div class="cell">40 years<span class="info">i</span></div>
      <div class="cell">£4,800.00<span class="info">i</span></div>
      <div class="cell">24 months<span class="info">i</span></div>
      <div class="cell actions"><span class="btn-buy">BUY NOW<i class="caret"></i></span><span class="btn-more">MORE INFO<i class="caret"></i></span></div>
    </div>

    <div class="load-more">Load More Insurances</div>
  </div>
</section>

<section class="about abs">
  <h2 class="section-title" style="top:22px">About Our Company</h2>
  <div class="title-rule" style="top:76px"></div>
  <p class="intro" style="top:97px">SilverQuoteWay is a new service set up to help you compare Guaranteed Life Cover. The service we offer is<br>free and without obligation to buy.</p>
  <p class="intro" style="top:153px">Our company also runs other websites you may be interested in <a>www.ambervalecover.com</a> and<br><a>www.greyharbourcover.com</a>, why not have visit!</p>
  <div class="cta-btn">Get Your Free Quote</div>
</section>

<footer class="site-footer abs">
  <div class="brand"><span>SilverQuoteWay.com</span><span class="brand-dot"></span></div>
  <div class="helpline">Lets Talk: <strong>0800 317 2946</strong></div>
  <div class="dash" style="top:97px"></div>
  <h3 class="club-title">Join The Club</h3>
  <p class="club-text">To the over 50s club for more information and offers subscribe us. Just type your email id and hit SUBSCRIBE button, that's it.</p>
  <div class="signup"><div class="email">Type your email is</div><div class="subscribe">Subscribe</div></div>
  <div class="dash" style="top:272px"></div>
  <p class="queries">For any other q ueries please mail us at <a>info@greyharbourcover.com</a></p>
</footer>

<div class="bottom-bar abs">
  <div class="legal-links"><span>Contact Us</span><span class="sep">|</span><span>Privacy Policy</span><span class="sep">|</span><span>T&amp;C's</span><span class="sep">|</span><span>About</span><span class="sep">|</span><span>Cookies</span></div>
  <p class="copyright">All content © 2016 SilverQuoteWay.com. This site is owned and managed by Daniel Harwood (info@ambervalecover.com). SilverQuoteWay works with Brightwell</p>
</div>

</body>
</html>
```